Brochure design for 3D ultrasound company

I am looking for a clean and modern and edgy brochure for my ultrasound company. We are a fairly new company specialize in 3D/4D ultrasounds.Our brochures will be placed in OB-GYN offices in high end areas around Los Angeles, so we need something that will stand out and capture a modern woman's attention. Our logo is currently in the process of being designed, so I don't have a picture to provide quite yet, however it will be our company name"Kite + Fern" written in a special font that looks like neon lights. I will attach a few images of what our logo will be like, and some initial content that can help provide the layout we would like for the brochure. please feel free to also take a look at our website. www.kitefernscans.example.

Target Market(s)

Upscale trendy women.

Colors
eea4c8
33a6d7
fee18a

Requirements
Should not have
• too many colors.

```html
<!DOCTYPE html>
<html lang="en">
<head>
<meta charset="utf-8">
<title>Kite + Fern — Services + Pricing</title>
<link rel="stylesheet" href="https://fonts.googleapis.com/css2?family=Oswald:wght@400;500&family=Alegreya+Sans+SC:wght@400&family=Alegreya+Sans:wght@400&family=Comfortaa:wght@400&display=swap">
<style>
:root{
  --brown:#574a3c;
  --ink:#2f2f2f;
  --coral:#f47c7c;
  --coral-text:#f2787a;
  --blush:#fccbca;
  --mist:#ececec;
  --grey-text:#a3a3a3;
  --dash:#a8a8a8;
  --rule:#ddd6b8;
  --white:#ffffff;
}
*{margin:0;padding:0;box-sizing:border-box}
html,body{width:1200px;height:783px;overflow:hidden;background:var(--white)}
.brochure{position:relative;width:1200px;height:783px;overflow:hidden;background:var(--white);font-family:"Alegreya Sans SC",sans-serif;color:var(--ink)}
.backdrop{position:absolute;inset:0}
.abs{position:absolute}
.hero-photo{left:0;top:0;width:402px;height:470px;
  background:
   linear-gradient(to bottom,rgba(255,255,255,0) 55%,#fff 100%),
   radial-gradient(ellipse at 45% 35%,#e9b6c2 0%,#c98c9f 30%,rgba(70,80,60,.0) 60%),
   linear-gradient(135deg,#2e3a2c,#4d5a44 50%,#d8a3b2 100%)}
.hero-title{left:0;width:412px;top:234px;text-align:center;font-family:"Oswald",sans-serif;font-weight:500;font-size:31px;color:var(--brown);letter-spacing:-.3px;transform:scaleX(.9)}
.feature-box{left:26px;top:281px;width:354px;height:267px;border:1px dashed var(--dash);background:rgba(255,255,255,.55)}
.feature-name{left:37px;top:297px;font-family:"Alegreya Sans",sans-serif;font-size:22px;text-transform:uppercase;color:#222}
.item{position:absolute;font-size:15.5px;white-space:nowrap;letter-spacing:.3px}
.item::before{content:"•";margin-right:5px;font-size:11px;vertical-align:2px}
.price{position:absolute;border-radius:50%;background:var(--coral);color:var(--white);font-family:"Comfortaa",sans-serif;font-size:21px;display:flex;align-items:center;justify-content:center}
.cta{position:absolute;left:0;width:392px;text-align:center;color:var(--grey-text);font-size:20.5px;line-height:26.5px;letter-spacing:.8px}
.main-title{left:438px;width:706px;top:28px;text-align:center;font-family:"Oswald",sans-serif;font-weight:500;font-size:50px;color:var(--brown);transform:scaleX(.92)}
.menu-box{left:438px;top:99px;width:706px;height:633px;border:1px dashed var(--dash)}
.menu-panel{left:439px;top:197px;width:704px;height:534px;background:rgba(255,255,255,.88)}
.intro{left:438px;width:706px;top:120px;text-align:center;font-size:19px;line-height:24px;letter-spacing:.6px}
.rule{position:absolute;left:448px;width:686px;border-top:1px dashed var(--rule)}
.package-name{position:absolute;left:457px;font-family:"Alegreya Sans",sans-serif;font-size:21px;text-transform:uppercase;color:var(--coral-text)}
.package-photo{position:absolute;border-radius:20px}
</style>
</head>
<body>
<main class="brochure">
  <svg class="backdrop" width="1200" height="783" viewBox="0 0 1200 783" aria-hidden="true">
    <polygon points="402,0 402,783 476,783 555,197 402,5" fill="var(--mist)"/>
    <polygon points="880,0 1200,0 1200,393" fill="var(--blush)"/>
    <polygon points="476,783 790,536 505,783" fill="var(--blush)"/>
  </svg>

  <section class="featured">
    <div class="abs hero-photo" role="img" aria-label="Expectant mother in a white dress covering her eyes amid pink smoke"></div>
    <h2 class="abs hero-title">OUR MOST POPULAR PACKAGE</h2>
    <div class="abs feature-box"></div>
    <h3 class="abs feature-name">The Big Reveal</h3>
    <p class="item" style="left:37px;top:330px">25 minute 3D/4D/HD live session</p>
    <p class="item" style="left:37px;top:354px">5 black and white pictures</p>
    <p class="item" style="left:37px;top:380px">5 color pictures</p>
    <p class="item" style="left:37px;top:404px">Email or USB flash drive with all images</p>
    <p class="item" style="left:37px;top:428px">Record and hear heartbeat</p>
    <p class="item" style="left:37px;top:453px">Confirm gender</p>
    <div class="price" style="left:262px;top:429px;width:104px;height:104px;font-size:22px">$225.00</div>

    <p class="cta" style="top:569px">Ready for your baby’s first<br>photoshoot?</p>
    <p class="cta" style="top:633px">Give us a call to schedule an<br>appointment (310) 555-0147</p>
    <p class="cta" style="top:698px">or visit our website<br>www.kitefernscans.example</p>
  </section>

  <section class="menu">
    <h1 class="abs main-title">SERVICES + PRICING</h1>
    <div class="abs menu-box"></div>
    <div class="abs menu-panel"></div>
    <p class="abs intro">We are available for private in-home screenings, gender reveals,<br>baby showers, or any other special occasion!</p>
    <div class="rule" style="top:197px"></div>

    <h3 class="package-name" style="top:211px">Peek-a-boo:</h3>
    <p class="item" style="left:457px;top:243px">15 minute 2D session</p>
    <p class="item" style="left:457px;top:272px">3 black and white images</p>
    <p class="item" style="left:457px;top:301px">Listen to baby’s heartbeat</p>
    <p class="item" style="left:457px;top:330px">Confirm gender</p>
    <div class="package-photo" style="left:845px;top:210px;width:195px;height:142px;background:linear-gradient(135deg,#c9a58c,#e3c4ae 50%,#bfa08a)" role="img" aria-label="Hands holding an ultrasound print against a pregnant belly"></div>
    <div class="price" style="left:1010px;top:270px;width:94px;height:94px">$125.00</div>
    <div class="rule" style="top:367px"></div>

    <h3 class="package-name" style="top:372px">Hello, Momma:</h3>
    <p class="item" style="left:457px;top:403px">15 minute 3D/4D /HD live session</p>
    <p class="item" style="left:457px;top:432px">3 black and white images</p>
    <p class="item" style="left:457px;top:461px">2 color images</p>
    <p class="item" style="left:457px;top:490px">Listen to baby’s heartbeat</p>
    <p class="item" style="left:457px;top:519px">Confirm gender</p>
    <div class="package-photo" style="left:847px;top:403px;width:195px;height:121px;background:linear-gradient(160deg,#f3ece9,#e9cdc3 45%,#d9a98f)" role="img" aria-label="Pregnant belly with a small plush toy resting on top"></div>
    <div class="price" style="left:1014px;top:440px;width:94px;height:94px">165.00</div>
    <div class="rule" style="top:548px"></div>

    <h3 class="package-name" style="top:552px">V.I.B (Very Important Baby):</h3>
    <p class="item" style="left:457px;top:583px">30 min 3D/4D/HD live session on our projector</p>
    <p class="item" style="left:457px;top:612px">10 color images</p>
    <p class="item" style="left:457px;top:641px">Email or USB with all images</p>
    <p class="item" style="left:457px;top:670px">Record and hear heartbeat</p>
    <p class="item" style="left:457px;top:699px">Confirm gender</p>
    <div class="package-photo" style="left:847px;top:563px;width:194px;height:143px;background:linear-gradient(135deg,#e4b79a,#9aa9bd 50%,#5d6f8c)" role="img" aria-label="Couple holding boy and girl notes over a pregnant belly in denim overalls"></div>
    <div class="price" style="left:1018px;top:620px;width:94px;height:94px">$325.00</div>
  </section>
</main>
</body>
</html>
```